Meadow Reset sale graphics for social media

You MUST read the Brief in the WORD document and follow the instructions there. I want to create 10 social media graphics (new Instagram size 4:5 (1080 x 1350 pixels) focusing on our Mother’s Day Meadow Reset Sale graphics, using any of the pics attached. Use the attached pics, NO RANDOM STOCK PHOTOGRAPHY. For the color scheme of the graphics, they should all be complementary to the product colors or feel like Spring time.

Target Market(s)

primarily women

Requirements
Must have
• the photos and text attached

```html
<!DOCTYPE html>
<html lang="en">
<head>
<meta charset="utf-8">
<title>Meadow Reset – Mother's Day Sale Graphics</title>
<link rel="stylesheet" href="https://fonts.googleapis.com/css2?family=Oswald:wght@500;600;700&family=Kaushan+Script&display=swap">
<style>
  :root{
    --pink:#e0336f;
    --green:#4f9a2a;
    --purple:#5a2e8e;
    --teal:#1f7f86;
    --white:#ffffff;
    --bg-blush:#fbe6ea;
    --bg-cream:#fbf9ee;
    --bg-lilac:#e9e1f3;
    --bg-mint:#eef5ef;
    --bg-butter:#fcf6e6;
    --bg-sky:#e2eff5;
    --bg-lime:#f1f5e2;
    --bg-rose:#fdeced;
  }
  *{margin:0;padding:0;box-sizing:border-box}
  html,body{width:1200px;height:1200px;overflow:hidden;background:#fff}
  body{position:relative;font-family:'Oswald',sans-serif;font-weight:600;text-transform:uppercase}
  .tile{position:absolute;display:flex;flex-direction:column;align-items:center;justify-content:center;text-align:center;line-height:.95;overflow:hidden}
  .tile.row{flex-direction:row;gap:14px}
  .badge{position:absolute;left:14px;top:14px;width:26px;height:26px;border-radius:50%;color:var(--white);font-size:15px;font-weight:700;display:flex;align-items:center;justify-content:center}
  .big{font-weight:700;letter-spacing:-2px;line-height:.85}
  .pct{font-weight:600}
  .script{font-family:'Kaushan Script',cursive;text-transform:none;font-weight:400;line-height:1.05}
  .brush{color:var(--white);padding:6px 22px;transform:rotate(-4deg);border-radius:4px 14px 6px 16px;margin:8px 0}
  .rule{display:flex;align-items:center;gap:8px;margin:10px 0}
  .rule span{display:block;height:2px;width:70px}
  .price{display:flex;align-items:flex-end}
  .stack{display:flex;flex-direction:column;align-items:flex-start;margin-left:4px}
  .divider{display:flex;flex-direction:column;align-items:center;align-self:stretch;justify-content:center;margin:30px 0}
  .divider span{width:2px;flex:1}
  .sprig{position:absolute;width:34px;height:16px;border-radius:50%;opacity:.35}
  .underline{height:3px;width:120px;border-radius:3px;margin-top:6px;transform:rotate(-3deg)}
</style>
</head>
<body>

<!-- 1 -->
<section class="tile" style="left:145px;top:30px;width:230px;height:474px;background:linear-gradient(#fbe3e8,#fdf1f2)">
  <div class="badge" style="background:var(--pink)">1</div>
  <div class="rule"><span style="background:var(--pink);width:30px"></span><svg width="16" height="14" viewBox="0 0 16 14"><path d="M8 14 1 7a4 4 0 0 1 7-5 4 4 0 0 1 7 5Z" fill="var(--pink)"/></svg><span style="background:var(--pink);width:30px"></span></div>
  <div style="color:var(--pink);font-size:32px">Mother’s Day</div>
  <div style="color:var(--green);font-size:58px;font-weight:700">Meadow</div>
  <div style="color:var(--pink);font-size:40px">Reset Sale</div>
  <div class="price" style="color:var(--purple);margin-top:8px"><span class="big" style="font-size:120px">25</span><span class="stack"><span class="pct" style="font-size:52px">%</span><span style="font-size:34px">Off</span></span></div>
  <div class="brush script" style="background:var(--pink);font-size:34px">Everything!</div>
</section>

<!-- 2 -->
<section class="tile" style="left:382px;top:30px;width:218px;height:474px;background:var(--bg-cream)">
  <div class="badge" style="background:var(--green)">2</div>
  <div class="sprig" role="img" aria-label="leaf sprig" style="left:26px;top:58px;background:var(--green)"></div>
  <div class="sprig" role="img" aria-label="leaf sprig" style="right:26px;top:58px;background:var(--green)"></div>
  <div class="price" style="color:var(--pink)"><span class="big" style="font-size:130px">25</span><span class="pct" style="font-size:90px;line-height:1">%</span></div>
  <div class="big" style="color:var(--pink);font-size:92px">Off</div>
  <div class="rule"><span style="background:var(--purple)"></span><svg width="18" height="16" viewBox="0 0 16 14"><path d="M8 14 1 7a4 4 0 0 1 7-5 4 4 0 0 1 7 5Z" fill="var(--purple)"/></svg><span style="background:var(--purple)"></span></div>
  <div style="color:var(--purple);font-size:28px">Mother’s Day</div>
  <div style="color:var(--green);font-size:46px;font-weight:700">Meadow</div>
  <div style="color:var(--pink);font-size:36px">Reset Sale</div>
</section>

<!-- 3 -->
<section class="tile" style="left:607px;top:30px;width:218px;height:474px;background:linear-gradient(#e6dcf2,#efe9f6)">
  <div class="badge" style="background:var(--purple)">3</div>
  <svg style="position:absolute;right:26px;top:44px" width="40" height="30" viewBox="0 0 40 30"><path d="M12 0l3 9 9 3-9 3-3 9-3-9-9-3 9-3z" fill="var(--purple)"/><path d="M32 14l2 5 5 2-5 2-2 5-2-5-5-2 5-2z" fill="var(--purple)"/></svg>
  <div class="price" style="color:var(--purple)"><span class="big" style="font-size:130px">25</span><span class="pct" style="font-size:90px;line-height:1">%</span></div>
  <div class="big" style="color:var(--purple);font-size:90px">Off</div>
  <div class="brush" style="background:var(--purple);font-size:38px;font-style:italic;font-weight:700;padding:4px 70px">All</div>
  <div style="color:var(--purple);font-size:30px">Supplements</div>
  <div class="script" style="color:var(--green);font-size:30px;margin-top:8px;transform:rotate(-6deg)">Meadow<br>Reset Sale!</div>
  <div class="underline" style="background:var(--green)"></div>
</section>

<!-- 4 -->
<section class="tile" style="left:833px;top:30px;width:230px;height:474px;background:var(--bg-mint)">
  <div class="badge" style="background:var(--teal)">4</div>
  <div class="sprig" role="img" aria-label="leaf sprig" style="left:30px;top:60px;background:var(--teal)"></div>
  <div class="sprig" role="img" aria-label="leaf sprig" style="right:44px;top:56px;background:var(--teal)"></div>
  <div class="price" style="color:var(--teal)"><span class="big" style="font-size:130px">25</span><span class="pct" style="font-size:90px;line-height:1">%</span></div>
  <div class="big" style="color:var(--teal);font-size:92px">Off</div>
  <div class="rule"><span style="background:var(--teal)"></span><svg width="18" height="16" viewBox="0 0 16 14"><path d="M8 14 1 7a4 4 0 0 1 7-5 4 4 0 0 1 7 5Z" fill="var(--teal)"/></svg><span style="background:var(--teal)"></span></div>
  <div style="color:var(--pink);font-size:34px">Meadow<br>Reset Sale:</div>
  <div style="color:var(--teal);font-size:28px;margin-top:6px">Spring Reset.</div>
  <div style="color:var(--purple);font-size:28px">Summer Ready</div>
</section>

<!-- 5 -->
<section class="tile" style="left:145px;top:512px;width:230px;height:407px;background:var(--bg-butter)">
  <div class="badge" style="background:var(--pink)">5</div>
  <div class="price" style="color:var(--pink)"><span class="big" style="font-size:112px">25</span><span class="pct" style="font-size:80px;line-height:1">%</span></div>
  <div class="big" style="color:var(--pink);font-size:80px">Off</div>
  <div class="brush" style="background:var(--pink);font-size:30px;font-style:italic;font-weight:700">Everything:</div>
  <div style="color:var(--purple);font-size:27px">Mother’s Day</div>
  <div style="color:var(--green);font-size:23px">Meadow Reset Sale</div>
  <div class="rule"><span style="background:var(--pink);width:56px"></span><svg width="16" height="14" viewBox="0 0 16 14"><path d="M8 14 1 7a4 4 0 0 1 7-5 4 4 0 0 1 7 5Z" fill="var(--pink)"/></svg><span style="background:var(--pink);width:56px"></span></div>
</section>

<!-- 6 -->
<section class="tile" style="left:382px;top:512px;width:218px;height:407px;background:linear-gradient(#dfeef6,#eaf3f7)">
  <div class="badge" style="background:var(--teal)">6</div>
  <div class="price" style="color:var(--teal)"><span class="big" style="font-size:112px">25</span><span class="pct" style="font-size:80px;line-height:1">%</span></div>
  <div class="big" style="color:var(--teal);font-size:80px">Off</div>
  <div class="rule"><span style="background:var(--teal)"></span><svg width="16" height="14" viewBox="0 0 16 14"><path d="M8 14 1 7a4 4 0 0 1 7-5 4 4 0 0 1 7 5Z" fill="var(--teal)"/></svg><span style="background:var(--teal)"></span></div>
  <div style="color:var(--teal);font-size:22px">Mother’s Day Sale:</div>
  <div class="script" style="color:var(--purple);font-size:32px;margin-top:6px;transform:rotate(-4deg)">Feel Amazing</div>
  <div style="color:var(--pink);font-size:42px;font-weight:700">Again!</div>
  <div class="underline" style="background:var(--teal)"></div>
</section>

<!-- 7 -->
<section class="tile" style="left:607px;top:512px;width:218px;height:407px;background:var(--bg-lime)">
  <div class="badge" style="background:var(--green)">7</div>
  <div class="sprig" role="img" aria-label="leaf sprig" style="left:30px;top:50px;background:var(--green)"></div>
  <div class="sprig" role="img" aria-label="leaf sprig" style="right:30px;top:46px;background:var(--green)"></div>
  <div class="price" style="color:var(--green)"><span class="big" style="font-size:112px">25</span><span class="pct" style="font-size:80px;line-height:1">%</span></div>
  <div class="big" style="color:var(--green);font-size:80px">Off</div>
  <div class="rule"><span style="background:var(--green)"></span><svg width="16" height="14" viewBox="0 0 16 14"><path d="M8 14 1 7a4 4 0 0 1 7-5 4 4 0 0 1 7 5Z" fill="var(--green)"/></svg><span style="background:var(--green)"></span></div>
  <div style="color:var(--green);font-size:22px">Mother’s Day Sale:</div>
  <div class="script" style="color:var(--green);font-size:38px;margin-top:6px;transform:rotate(-4deg)">Refresh</div>
  <div class="script" style="color:var(--teal);font-size:36px;transform:rotate(-4deg)">Your Body</div>
  <div class="underline" style="background:var(--green)"></div>
</section>

<!-- 8 -->
<section class="tile" style="left:833px;top:512px;width:230px;height:407px;background:var(--bg-rose)">
  <div class="badge" style="background:var(--pink)">8</div>
  <div class="price" style="color:var(--pink)"><span class="big" style="font-size:112px">25</span><span class="pct" style="font-size:80px;line-height:1">%</span></div>
  <div class="big" style="color:var(--pink);font-size:80px">Off</div>
  <div style="color:var(--pink);font-size:22px;margin-top:18px">Meadow Reset Sale:</div>
  <div style="color:var(--green);font-size:31px;margin-top:6px">Spring Cleanse.</div>
  <div style="color:var(--purple);font-size:31px">Summer Glow</div>
  <div class="rule"><span style="background:var(--pink)"></span><svg width="16" height="14" viewBox="0 0 16 14"><path d="M8 14 1 7a4 4 0 0 1 7-5 4 4 0 0 1 7 5Z" fill="var(--pink)"/></svg><span style="background:var(--pink)"></span></div>
</section>

<!-- 9 -->
<section class="tile row" style="left:145px;top:928px;width:459px;height:250px;background:linear-gradient(#f8d5de,#fce9ec)">
  <div class="badge" style="background:var(--pink)">9</div>
  <div class="sprig" role="img" aria-label="leaf sprig" style="left:70px;top:24px;background:var(--pink)"></div>
  <div class="price" style="color:var(--pink)"><span class="big" style="font-size:120px">25</span><span class="stack"><span class="pct" style="font-size:56px">%</span><span style="font-size:30px">Off</span></span></div>
  <div class="divider"><span style="background:var(--pink)"></span><svg width="14" height="12" viewBox="0 0 16 14"><path d="M8 14 1 7a4 4 0 0 1 7-5 4 4 0 0 1 7 5Z" fill="var(--pink)"/></svg><span style="background:var(--pink)"></span></div>
  <div style="display:flex;flex-direction:column;align-items:center">
    <div style="color:var(--pink);font-size:24px">Mother’s Day Sale:</div>
    <div style="color:var(--green);font-size:24px;margin-top:6px">Detox This Spring.</div>
    <div class="script" style="color:var(--pink);font-size:34px;margin-top:4px;transform:rotate(-4deg)">Shine This<br>Summer</div>
    <div class="underline" style="background:var(--pink);width:130px"></div>
  </div>
</section>

<!-- 10 -->
<section class="tile row" style="left:612px;top:928px;width:451px;height:250px;background:linear-gradient(135deg,#d8ecf3,#eef6f4)">
  <div class="badge" style="background:var(--teal)">10</div>
  <div class="price" style="color:var(--teal)"><span class="big" style="font-size:120px">25</span><span class="stack"><span class="pct" style="font-size:56px">%</span><span style="font-size:30px">Off</span></span></div>
  <div class="divider"><span style="background:var(--teal)"></span><svg width="14" height="12" viewBox="0 0 16 14"><path d="M8 14 1 7a4 4 0 0 1 7-5 4 4 0 0 1 7 5Z" fill="var(--teal)"/></svg><span style="background:var(--teal)"></span></div>
  <div style="display:flex;flex-direction:column;align-items:center">
    <div style="color:var(--teal);font-size:24px">Mother’s Day Sale:</div>
    <div style="color:var(--green);font-size:33px;margin-top:6px">Meadow Reset</div>
    <div class="rule" style="margin:2px 0"><span style="background:var(--teal);width:50px;height:1px"></span><span class="script" style="color:var(--teal);font-size:24px;width:auto;height:auto;background:none">for a</span><span style="background:var(--teal);width:50px;height:1px"></span></div>
    <div style="color:var(--purple);font-size:33px">Summer Body</div>
    <div class="underline" style="background:var(--teal);width:150px"></div>
  </div>
</section>

</body>
</html>
```